Investor deck - offshore energy

I'm building a pitch deck to show to investors (banks, private equity) interested in acquiring existing offshore oil and gas properties. I need a basic logo for the company: "Quillmore Partners". It's an LLC. It'll be an Exploration & Production company (E&P) so the first letters of the industry coincidentally match up with the name of the LLC. Feel free to play with that on the logo, or not. More importantly, I need a powerpoint design for a ~40 slide presentation. The audience will be both financial and engineering professionals, so the design needs to appeal to both. The template design should leave a lot of space for the content. The font needs to be easy to read and not fancy. A white background is a must I would think. Be aware, I'll be adding many tables, timelines, and charts. Considering it's an offshore energy pitch, a color scheme that includes blue would make sense, but I am flexible to consider other options. Potential for considerable additional design support if the pitch is successful. Thank you.

Target Market(s)

Banks, private equity, CFOs, COOs, CEOs, engineers

Industry/Entity Type

Energy - Oil & Gas

Font styles to use
Sans Serif
Other font styles liked:
• Open to other easy-to-read, professional, and available fonts

Requirements
Must have
• A logo, powerpoint design template, appropriate color and font scheme
Nice to have
• Chart designs and table designs
Should not have
• Real pictures. I'll add any of those myself. I've included some concept "inspirational photos" for the design considerations.

```html
<!DOCTYPE html>
<html lang="en">
<head>
<meta charset="utf-8">
<title>Quillmore Partners LLC – Investor Deck Template</title>
<link href="https://fonts.googleapis.com/css2?family=Hind:wght@400;500;600;700&family=Roboto:wght@300;400;500;700&display=swap" rel="stylesheet">
<style>
:root{
  --green:#18a068;
  --teal:#158a8f;
  --blue:#1565c0;
  --dark:#474747;
  --ink:#2b2b2b;
  --muted:#7a7a7a;
  --canvas:#eef7f9;
  --white:#ffffff;
  --brand-grad:linear-gradient(90deg,var(--green) 0%,var(--teal) 50%,var(--blue) 100%);
}
*{box-sizing:border-box;margin:0;padding:0}
html,body{width:1200px;height:4051px;overflow:hidden}
body{background:var(--canvas);font-family:"Roboto",sans-serif;color:var(--ink);position:relative}
.slide{position:absolute;left:76px;width:1048px;height:590px;background:var(--white);overflow:hidden;box-shadow:0 4px 14px rgba(20,60,90,.12)}
.slide--cover{top:88px}
.slide--about{top:745px}
.slide--table{top:1402px}
.slide--charts{top:2059px}
.slide--timeline{top:2716px}
.slide--thanks{top:3373px}
.heading{font-family:"Hind",sans-serif}

/* Cover */
.cover-band{position:absolute;inset:0 0 auto 0;height:460px;background:linear-gradient(100deg,var(--green) 0%,#139185 40%,var(--blue) 100%)}
.cover-wave{position:absolute;left:0;top:0;width:1048px;height:590px}
.cover-mark{position:absolute;left:494px;top:58px;width:60px;height:60px;border:4px solid var(--white);border-radius:50%}
.cover-name{position:absolute;left:0;width:100%;top:200px;text-align:center;font-family:"Hind",sans-serif;font-weight:600;font-size:37px;color:var(--white);letter-spacing:.5px}
.cover-tag{position:absolute;left:0;width:100%;top:248px;display:flex;justify-content:center;align-items:center;gap:12px;font-family:"Hind",sans-serif;font-weight:500;font-size:17px;letter-spacing:2px;color:var(--white)}
.cover-tag::before,.cover-tag::after{content:"";width:50px;height:1.5px;background:var(--white)}
.cover-photo{position:absolute;left:646px;top:296px;width:264px;height:264px;border-radius:50%;background:var(--white);padding:12px;box-shadow:0 6px 16px rgba(0,0,0,.15)}
.cover-photo div{width:100%;height:100%;border-radius:50%;background:linear-gradient(180deg,#8fb4dd 0%,#d9b565 48%,#2f5f93 62%,#183f6e 100%)}
.welcome{position:absolute;left:61px;top:440px}
.welcome-kicker{font-family:"Hind",sans-serif;font-weight:500;font-size:21px;color:var(--green)}
.welcome-name{font-family:"Hind",sans-serif;font-weight:600;font-size:35px;color:var(--blue);line-height:1.15}
.welcome-tag{font-family:"Hind",sans-serif;font-weight:600;font-size:19px;color:var(--ink);letter-spacing:1px;margin-top:14px}

/* Shared inner slide chrome */
.brand{position:absolute;left:40px;top:10px;width:200px;text-align:center}
.brand-dot{width:30px;height:30px;border-radius:50%;border:3px solid var(--teal);margin:0 auto 8px}
.brand-name{font-family:"Hind",sans-serif;font-weight:500;font-size:12.5px;color:var(--ink);letter-spacing:.2px}
.brand-tag{display:flex;justify-content:center;align-items:center;gap:5px;font-size:6.5px;letter-spacing:1px;color:var(--muted);margin-top:1px}
.brand-tag::before,.brand-tag::after{content:"";width:22px;height:1px;background:#bbb}
.title-bar{position:absolute;left:338px;top:20px;width:710px;height:59px;border-radius:30px 0 0 30px;background:var(--brand-grad);display:flex;align-items:center;justify-content:space-between;padding:0 58px 0 25px}
.title-bar::before{content:"";width:12px;height:12px;border-radius:50%;background:var(--white)}
.title-bar h2{font-family:"Hind",sans-serif;font-weight:600;font-size:28px;color:var(--white);letter-spacing:.3px;padding-top:4px}
.page-no{position:absolute;right:58px;top:558px;font-size:12px;font-weight:700;color:var(--blue);letter-spacing:.5px}
.page-no span{color:#9ab;font-weight:400;margin:0 5px}
.foot-rule{position:absolute;left:0;bottom:0;width:100%;height:5px;background:linear-gradient(90deg,var(--dark) 0 857px,var(--green) 857px 100%)}

/* About */
.about-photo{position:absolute;left:61px;top:135px;width:463px;height:371px;border-radius:18px 60px 0 60px;background:linear-gradient(180deg,#6f5aa6 0%,#c87aa2 30%,#f2a15a 55%,#d8782e 65%,#3b2d45 100%)}
.about-copy{position:absolute;left:585px;top:176px;width:404px;font-size:12.6px;line-height:21.8px;color:var(--muted);text-align:justify}
.about-copy p+p{margin-top:12px}

/* Tabulation */
.tab-card{position:absolute;top:151px;width:235px;height:329px;background:var(--white);border-radius:10px;box-shadow:0 4px 16px rgba(30,60,90,.14);padding:24px 16px 0 20px;border-bottom:4px solid}
.tab-card--green{left:143px;border-color:var(--green)}
.tab-card--teal{left:407px;border-color:var(--teal)}
.tab-card--blue{left:671px;border-color:var(--blue)}
.tab-card h3{font-family:"Hind",sans-serif;font-weight:500;font-size:15px;line-height:22px;text-align:center;margin-bottom:28px}
.tab-card--green h3{color:var(--green)}
.tab-card--teal h3{color:var(--teal)}
.tab-card--blue h3{color:var(--blue)}
.tab-list{list-style:none}
.tab-list li{position:relative;padding-left:20px;font-size:10.5px;line-height:16px;color:var(--dark);margin-bottom:8px}
.tab-list li::before{content:"";position:absolute;left:0;top:3px;width:8px;height:8px;border:2px solid;border-radius:50%}
.tab-card--green li::before{border-color:var(--green)}
.tab-card--teal li::before{border-color:var(--teal)}
.tab-card--blue li::before{border-color:var(--blue)}

/* Charts */
.pie{position:absolute;left:66px;top:139px;width:380px;height:380px;filter:drop-shadow(0 6px 10px rgba(0,0,0,.15))}
.pie text{font-family:"Roboto",sans-serif;font-weight:300;font-size:25px;fill:var(--white)}
.legend-item{position:absolute;left:488px;width:480px;height:90px}
.legend-icon{position:absolute;left:0;top:0;width:68px;height:68px;border-radius:50%;background:var(--white);box-shadow:0 3px 10px rgba(0,0,0,.18);display:flex;align-items:center;justify-content:center}
.legend-icon span{width:56px;height:56px;border-radius:50%;display:flex;align-items:center;justify-content:center}
.legend-item h4{position:absolute;left:99px;top:-14px;font-size:13.5px;font-weight:500;color:var(--ink);letter-spacing:.3px}
.legend-item p{position:absolute;left:99px;top:13px;width:384px;font-size:12.6px;line-height:20px;color:var(--muted)}

/* Timeline */
.tl-arrows{position:absolute;left:0;top:0;width:1048px;height:590px}
.tl-step{position:absolute;top:200px;width:168px;text-align:center}
.tl-year{font-family:"Hind",sans-serif;font-weight:600;font-size:17px;height:36px}
.tl-card{position:relative;margin-top:31px;height:185px;background:var(--white);border-top:3px solid;border-radius:4px;box-shadow:0 4px 14px rgba(30,60,90,.13);padding:40px 12px 0}
.tl-badge{position:absolute;left:57px;top:-29px;width:54px;height:54px;border-radius:50%;border:3px solid var(--white);display:flex;align-items:center;justify-content:center;box-shadow:0 2px 6px rgba(0,0,0,.15)}
.tl-card h5{font-size:10px;line-height:16px;font-weight:700;color:var(--ink)}
.tl-card p{font-size:9.6px;line-height:15.5px;color:var(--dark);margin-top:8px}
.tl--green .tl-year{color:var(--green)} .tl--green .tl-card{border-color:var(--green)} .tl--green .tl-badge{background:var(--green)}
.tl--teal .tl-year{color:var(--teal)} .tl--teal .tl-card{border-color:var(--teal)} .tl--teal .tl-badge{background:var(--teal)}
.tl--blue .tl-year{color:var(--blue)} .tl--blue .tl-card{border-color:var(--blue)} .tl--blue .tl-badge{background:var(--blue)}

/* Thank you */
.thanks-bg{position:absolute;inset:0;background:linear-gradient(120deg,#12937a 0%,#1378a8 45%,var(--blue) 100%)}
.thanks-art{position:absolute;left:0;top:0;width:1048px;height:590px}
.thanks-title{position:absolute;left:671px;top:60px;font-family:"Hind",sans-serif;font-weight:600;font-size:46px;color:var(--white);letter-spacing:.5px}
.contact{position:absolute;left:685px;list-style:none;color:var(--white);font-size:14.5px;line-height:24px}
.contact li{position:absolute;left:0;width:320px;display:flex;gap:20px;align-items:flex-start}
.contact svg{flex:none;width:26px;height:26px}
.thanks-brand{position:absolute;left:732px;top:440px;width:200px;text-align:center}
.thanks-brand .brand-dot{width:44px;height:44px;border-width:4px;margin-bottom:14px}
.thanks-brand .brand-name{font-size:15.5px}
.thanks-brand .brand-tag{font-size:8px}
</style>
</head>
<body>

<!-- Slide 1: Cover -->
<section class="slide slide--cover">
  <div class="cover-band"></div>
  <svg class="cover-wave" viewBox="0 0 1048 590" aria-hidden="true">
    <path d="M0,402 C230,300 470,330 690,405 C840,455 950,420 1048,370 L1048,395 C950,445 840,480 690,430 C470,355 230,330 0,430 Z" fill="#c9c9c9"/>
    <path d="M0,420 C230,330 470,352 690,425 C840,472 950,438 1048,390 L1048,590 L0,590 Z" fill="#ffffff"/>
  </svg>
  <div class="cover-mark"></div>
  <div class="cover-name">QUILLMORE PARTNERS LLC</div>
  <div class="cover-tag">EXPLORATION &amp; PRODUCTION</div>
  <div class="cover-photo"><div role="img" aria-label="Offshore oil platform standing in open sea under a clear sky"></div></div>
  <div class="welcome">
    <div class="welcome-kicker">WELCOME TO</div>
    <div class="welcome-name">QUILLMORE PARTNERS LLC</div>
    <div class="welcome-tag">EXPLORATION &amp; PRODUCTION</div>
  </div>
</section>

<!-- Slide 2: About us -->
<section class="slide slide--about">
  <div class="brand"><div class="brand-dot"></div><div class="brand-name">QUILLMORE PARTNERS LLC</div><div class="brand-tag">EXPLORATION &amp; PRODUCTION</div></div>
  <div class="title-bar"><h2>ABOUT US</h2></div>
  <div class="about-photo" role="img" aria-label="Offshore production platform at sunset over the sea"></div>
  <div class="about-copy">
    <p>Lorem ipsum dolor sit amet, consectetur adipiscing elit, sed do eiusmod tempor incididunt ut labore et dolore magna aliqua. Ut enim ad minim veniam, quis nostrud exercitation ullamco lab oris nisi ut aliquip ex ea commodo consequat. Duis aute irure dolor in reprehenderit in voluptate velit esse cillum dolore eu fugiat nulla pariatur excepteurea.</p>
    <p>Lorem ipsum dolor sit amet, consectetur adipiscing elit, sed do eiusmod tempor incididunt ut labore et dolore magna aliqua. Ut enim ad minim veniam, quis nostrud exercitation ullamco lab oris nisi ut aliquip ex ea comea.</p>
    <p>Lorem ipsum dolor sit amet, consectetur adipiscing elit, sed do eiusmod tempor incididuntea.</p>
  </div>
  <div class="page-no">PAGE<span>|</span>02</div>
  <div class="foot-rule"></div>
</section>

<!-- Slide 3: Tabulation -->
<section class="slide slide--table">
  <div class="brand"><div class="brand-dot"></div><div class="brand-name">QUILLMORE PARTNERS LLC</div><div class="brand-tag">EXPLORATION &amp; PRODUCTION</div></div>
  <div class="title-bar"><h2>TABULATION</h2></div>
  <article class="tab-card tab-card--green">
    <h3>LOREM IPSUM DOL<br>ORSIT AMET</h3>
    <ul class="tab-list">
      <li>Lorem ipsum dolor sit amet, cons ectetur adipisea</li>
      <li>Sed ut perspiciatis unde omnis is tenatus error</li>
      <li>Lorem ipsum dolor sit amet</li>
      <li>Sed ut perspiciatis unde omnis</li>
      <li>Lorem ipsum dolor sit amet, cons ectetur adipisea</li>
      <li>Sed ut perspiciatis unde omnis is tenatus error</li>
    </ul>
  </article>
  <article class="tab-card tab-card--teal">
    <h3>LOREM IPSUM DOL<br>ORSIT AMET</h3>
    <ul class="tab-list">
      <li>Lorem ipsum dolor sit amet, cons ectetur adipisea</li>
      <li>Sed ut perspiciatis unde omnis is tenatus error</li>
      <li>Lorem ipsum dolor sit amet</li>
      <li>Sed ut perspiciatis unde omnis</li>
      <li>Lorem ipsum dolor sit amet, cons ectetur adipisea</li>
      <li>Sed ut perspiciatis unde omnis is tenatus error</li>
    </ul>
  </article>
  <article class="tab-card tab-card--blue">
    <h3>LOREM IPSUM DOL<br>ORSIT AMET</h3>
    <ul class="tab-list">
      <li>Lorem ipsum dolor sit amet, cons ectetur adipisea</li>
      <li>Sed ut perspiciatis unde omnis is tenatus error</li>
      <li>Lorem ipsum dolor sit amet</li>
      <li>Sed ut perspiciatis unde omnis</li>
      <li>Lorem ipsum dolor sit amet, cons ectetur adipisea</li>
      <li>Sed ut perspiciatis unde omnis is tenatus error</li>
    </ul>
  </article>
  <div class="page-no">PAGE<span>|</span>03</div>
  <div class="foot-rule"></div>
</section>

<!-- Slide 4: Charts -->
<section class="slide slide--charts">
  <div class="brand"><div class="brand-dot"></div><div class="brand-name">QUILLMORE PARTNERS LLC</div><div class="brand-tag">EXPLORATION &amp; PRODUCTION</div></div>
  <div class="title-bar"><h2>OUR CHARTS</h2></div>
  <svg class="pie" viewBox="-190 -190 380 380" role="img" aria-label="Pie chart: 59%, 18%, 10%, 13%">
    <g stroke="#ffffff" stroke-width="2">
      <path d="M0,0 L0,-178 A178,178 0 1,1 -95.4,150.3 Z" fill="var(--dark)"/>
      <path d="M0,0 L-95.4,150.3 A178,178 0 0,1 -176.6,-22.3 Z" fill="var(--blue)"/>
      <path d="M0,0 L-176.6,-22.3 A178,178 0 0,1 -129.8,-121.8 Z" fill="var(--green)"/>
      <path d="M0,0 L-129.8,-121.8 A178,178 0 0,1 0,-178 Z" fill="var(--teal)"/>
    </g>
    <g text-anchor="middle">
      <text x="104" y="33">59%</text>
      <text x="-96" y="60">18%</text>
      <text x="-123" y="-39">10%</text>
      <text x="-50" y="-112">13%</text>
    </g>
  </svg>

  <div class="legend-item" style="top:137px">
    <div class="legend-icon"><span style="background:var(--green)"><svg width="30" height="30" viewBox="0 0 30 30" fill="none" stroke="#fff" stroke-width="2"><rect x="5" y="16" width="4" height="9"/><rect x="13" y="11" width="4" height="14"/><rect x="21" y="6" width="4" height="19"/></svg></span></div>
    <h4>LOREM IPSUM DOLOR (10%)</h4>
    <p>Lorem ipsum dolor sit amet, consectetur adipiscing elitsed do eiusmod tempor incidiea.</p>
  </div>
  <div class="legend-item" style="top:241px">
    <div class="legend-icon"><span style="background:var(--teal)"><svg width="30" height="30" viewBox="0 0 30 30" fill="none" stroke="#fff" stroke-width="2"><circle cx="13" cy="13" r="8"/><path d="M19 19l7 7"/></svg></span></div>
    <h4>LOREM IPSUM DOLOR (13%)</h4>
    <p>Lorem ipsum dolor sit amet, consectetur adipiscing elitsed do eiusmod tempor incidiea.</p>
  </div>
  <div class="legend-item" style="top:345px">
    <div class="legend-icon"><span style="background:var(--blue)"><svg width="30" height="30" viewBox="0 0 30 30" fill="none" stroke="#fff" stroke-width="2"><circle cx="15" cy="15" r="5"/><path d="M15 3v4M15 23v4M3 15h4M23 15h4M6.5 6.5l3 3M20.5 20.5l3 3M6.5 23.5l3-3M20.5 9.5l3-3"/></svg></span></div>
    <h4>LOREM IPSUM DOLOR (18%)</h4>
    <p>Lorem ipsum dolor sit amet, consectetur adipiscing elitsed do eiusmod tempor incidiea.</p>
  </div>
  <div class="legend-item" style="top:449px">
    <div class="legend-icon"><span style="background:var(--dark)"><svg width="30" height="30" viewBox="0 0 30 30" fill="none" stroke="#fff" stroke-width="2"><rect x="6" y="4" width="18" height="22" rx="2"/><path d="M10 10h10M10 15h10M10 20h6"/></svg></span></div>
    <h4>LOREM IPSUM DOLOR (59%)</h4>
    <p>Lorem ipsum dolor sit amet, consectetur adipiscing elitsed do eiusmod tempor incidiea.</p>
  </div>
  <div class="page-no">PAGE<span>|</span>04</div>
  <div class="foot-rule"></div>
</section>

<!-- Slide 5: Timelines -->
<section class="slide slide--timeline">
  <div class="brand"><div class="brand-dot"></div><div class="brand-name">QUILLMORE PARTNERS LLC</div><div class="brand-tag">EXPLORATION &amp; PRODUCTION</div></div>
  <div class="title-bar"><h2>TIMELINES</h2></div>
  <svg class="tl-arrows" viewBox="0 0 1048 590" aria-hidden="true">
    <defs>
      <marker id="tl-head" viewBox="0 0 10 10" refX="3" refY="5" markerWidth="4" markerHeight="4" orient="auto"><path d="M0,0 L10,5 L0,10 Z" fill="#d9dcdf"/></marker>
    </defs>
    <g fill="none" stroke="#d9dcdf" stroke-width="8" stroke-linecap="round" marker-end="url(#tl-head)">
      <path d="M362,170 Q430,120 492,150"/>
      <path d="M740,170 Q808,120 870,150"/>
      <path d="M175,510 Q245,535 305,495"/>
      <path d="M552,510 Q622,535 682,495"/>
    </g>
  </svg>
  <div class="tl-step tl--green" style="left:61px"><div class="tl-year">2020</div><div class="tl-card"><div class="tl-badge"><svg width="24" height="24" viewBox="0 0 24 24" fill="none" stroke="#fff" stroke-width="1.8"><rect x="3" y="13" width="4" height="8"/><rect x="10" y="8" width="4" height="13"/><rect x="17" y="3" width="4" height="18"/></svg></div><h5>LOREM IPSUM DOLOR<br>SIT AMET</h5><p>Lorem ipsum dolor sit amet, consectetur adipiscing elit, sed do eiusmod tempor incididunt ut labore et dolore magna aliqua ut enimea.</p></div></div>
  <div class="tl-step tl--teal" style="left:250px"><div class="tl-year">2021</div><div class="tl-card"><div class="tl-badge"><svg width="24" height="24" viewBox="0 0 24 24" fill="none" stroke="#fff" stroke-width="1.8"><rect x="4" y="4" width="7" height="7"/><rect x="13" y="4" width="7" height="7"/><rect x="4" y="13" width="7" height="7"/><rect x="13" y="13" width="7" height="7"/></svg></div><h5>LOREM IPSUM DOLOR<br>SIT AMET</h5><p>Lorem ipsum dolor sit amet, consectetur adipiscing elit, sed do eiusmod tempor incididunt ut labore et dolore magna aliqua ut enimea.</p></div></div>
  <div class="tl-step tl--blue" style="left:440px"><div class="tl-year">2022</div><div class="tl-card"><div class="tl-badge"><svg width="24" height="24" viewBox="0 0 24 24" fill="none" stroke="#fff" stroke-width="1.8"><rect x="5" y="3" width="14" height="18" rx="2"/><path d="M8 8h8M8 12h8M8 16h5"/></svg></div><h5>LOREM IPSUM DOLOR<br>SIT AMET</h5><p>Lorem ipsum dolor sit amet, consectetur adipiscing elit, sed do eiusmod tempor incididunt ut labore et dolore magna aliqua ut enimea.</p></div></div>
  <div class="tl-step tl--teal" style="left:630px"><div class="tl-year">2023</div><div class="tl-card"><div class="tl-badge"><svg width="24" height="24" viewBox="0 0 24 24" fill="none" stroke="#fff" stroke-width="1.8"><rect x="3" y="5" width="18" height="12" rx="1"/><path d="M8 21h8M12 17v4"/></svg></div><h5>LOREM IPSUM DOLOR<br>SIT AMET</h5><p>Lorem ipsum dolor sit amet, consectetur adipiscing elit, sed do eiusmod tempor incididunt ut labore et dolore magna aliqua ut enimea.</p></div></div>
  <div class="tl-step tl--green" style="left:818px"><div class="tl-year">2024</div><div class="tl-card"><div class="tl-badge"><svg width="24" height="24" viewBox="0 0 24 24" fill="none" stroke="#fff" stroke-width="1.8"><circle cx="12" cy="12" r="8"/><circle cx="12" cy="12" r="3"/></svg></div><h5>LOREM IPSUM DOLOR<br>SIT AMET</h5><p>Lorem ipsum dolor sit amet, consectetur adipiscing elit, sed do eiusmod tempor incididunt ut labore et dolore magna aliqua ut enimea.</p></div></div>
  <div class="page-no">PAGE<span>|</span>05</div>
  <div class="foot-rule"></div>
</section>

<!-- Slide 6: Thank you -->
<section class="slide slide--thanks">
  <div class="thanks-bg"></div>
  <svg class="thanks-art" viewBox="0 0 1048 590">
    <defs>
      <linearGradient id="rig-tone" x1="0" y1="0" x2="0" y2="1">
        <stop offset="0" stop-color="#9db6cf"/>
        <stop offset=".45" stop-color="#d8b456"/>
        <stop offset=".65" stop-color="#6f8aa6"/>
        <stop offset="1" stop-color="#2c3f57"/>
      </linearGradient>
    </defs>
    <path d="M0,500 C250,600 650,560 1048,420 L1048,452 C650,585 250,615 0,540 Z" fill="var(--green)"/>
    <path d="M0,540 C250,615 650,585 1048,452 L1048,590 L0,590 Z" fill="#ffffff"/>
    <circle cx="239" cy="181" r="352" fill="var(--green)"/>
    <circle cx="239" cy="181" r="334" fill="#ffffff"/>
    <circle cx="239" cy="181" r="316" fill="url(#rig-tone)" role="img" aria-label="Offshore oil platform lit at dusk above calm water"/>
  </svg>
  <h2 class="thanks-title">THANK YOU</h2>
  <ul class="contact">
    <li style="top:158px"><svg viewBox="0 0 24 24" fill="none" stroke="#fff" stroke-width="1.8"><path d="M5 3h4l2 5-2.5 1.5a11 11 0 0 0 6 6L16 13l5 2v4a2 2 0 0 1-2 2A17 17 0 0 1 3 5a2 2 0 0 1 2-2z"/></svg><span>+1 (888) 888 8888</span></li>
    <li style="top:204px"><svg viewBox="0 0 24 24" fill="none" stroke="#fff" stroke-width="1.8"><circle cx="12" cy="12" r="9"/><path d="M3 12h18M12 3c3 3 3 15 0 18M12 3c-3 3-3 15 0 18"/></svg><span>https://QuillmorePartnersLLC.com/</span></li>
    <li style="top:248px"><svg viewBox="0 0 24 24" fill="none" stroke="#fff" stroke-width="1.8"><rect x="3" y="6" width="18" height="13"/><path d="M3 6l9 7 9-7"/></svg><span>info@QuillmorePartnersLLC.com</span></li>
    <li style="top:294px"><svg viewBox="0 0 24 24" fill="none" stroke="#fff" stroke-width="1.8"><path d="M12 22s7-7 7-12a7 7 0 0 0-14 0c0 5 7 12 7 12z"/><circle cx="12" cy="10" r="2.5"/></svg><span>465, Lorum Ipsum Dolore Sed Amet<br>United States</span></li>
  </ul>
  <div class="thanks-brand"><div class="brand-dot"></div><div class="brand-name">QUILLMORE PARTNERS LLC</div><div class="brand-tag">EXPLORATION &amp; PRODUCTION</div></div>
</section>

</body>
</html>
```